Eycatcher Flyer
Zielgruppe
Infos auf www.lumawerk-beratung.ch
Lebensberatung, Seminare, persönliche Weiterbildung,Medium
Aufgabenstellung
Suche ein Design für einen coolen, modernen, mystischen exklusiven(Image) Flyer. Format A4 Längs gefaltet (Endformat A5).
Flyer Titel Liebe dein Leben - Liebe dich selbst eventuell auch auf englisch love yourself and celebrates your life
oder vielleicht hat jemand noch einen besseren Slogan Vorschlag
Habe im Anhang ein Dokument mit Text kann ganz oder auszugweise verwendet werden. (Handelt sich um einen ersten Entwurf mögliche Rechtschreibfehler enthalten)
Ansonsten Inputs aus der Hp holen.
Lieblingsfarben Rot,Pink,Giftgrün,Gold,Schwarz, Gelb,

```html
<!DOCTYPE html>
<html lang="de">
<head>
<meta charset="utf-8">
<title>Liebe Dich Selbst – Flyer</title>
<link rel="stylesheet" href="https://fonts.googleapis.com/css2?family=Pinyon+Script&family=Questrial&display=swap">
<style>
  :root {
    --paper: #ffffff;
    --ink-brown: #8a6a3c;
    --ink-soft: #9a7a4c;
    --fold-line: #4a4a4a;
    --edge-grey: #6e6e6e;
    --accent-berry: #a3174a;
    --photo-light: #d8c2a2;
    --photo-mid: #b39066;
    --photo-dark: #6f5236;
  }
  * { margin: 0; padding: 0; box-sizing: border-box; }
  html, body { width: 1200px; height: 852px; overflow: hidden; background: var(--paper); }
  body { font-family: "Questrial", "Century Gothic", sans-serif; color: var(--ink-brown); }

  .flyer { position: relative; width: 1200px; height: 852px; background: var(--paper); }
  .flyer::after {
    content: ""; position: absolute; left: 0; right: 0; bottom: 0; height: 3px; background: var(--edge-grey);
  }

  .panel { position: absolute; top: 0; height: 849px; }
  .panel--back { left: 0; width: 589px; border-right: 1px solid var(--fold-line); }
  .panel--front { left: 590px; width: 610px; }

  .ornament-slot {
    position: absolute; left: 276px; top: 124px; width: 40px; height: 40px; border-radius: 50%;
    background: radial-gradient(circle, var(--ink-soft) 0%, rgba(154,122,76,0.25) 70%, transparent 72%);
  }

  .quote { position: absolute; left: 40px; width: 510px; top: 188px; text-align: center;
    font-size: 19px; line-height: 24px; letter-spacing: 0.2px; }
  .quote p + p { margin-top: 24px; }
  .initial { font-family: "Pinyon Script", cursive; font-size: 44px; line-height: 0; vertical-align: -4px; }

  .contact { position: absolute; left: 40px; width: 510px; top: 640px; text-align: center;
    font-size: 19px; line-height: 24px; }
  .contact p + p { margin-top: 24px; }

  .photo { position: absolute; left: 0; top: 0; width: 610px; height: 360px;
    background: radial-gradient(ellipse at 45% 45%, var(--photo-light) 0%, var(--photo-mid) 55%, var(--photo-dark) 100%); }

  .title { position: absolute; left: 0; width: 610px; top: 420px; text-align: center;
    font-size: 36px; letter-spacing: 0.5px; font-weight: normal; }
  .title .initial { font-size: 86px; vertical-align: -8px; }

  .tagline { position: absolute; left: 0; width: 610px; top: 543px; text-align: center;
    font-size: 19px; letter-spacing: 0.6px; }

  .brand { position: absolute; left: 200px; top: 700px; display: flex; align-items: center; gap: 14px; }
  .brand__dot { width: 46px; height: 46px; border-radius: 50%; background: var(--accent-berry); }
  .brand__name { font-size: 34px; color: var(--ink-brown); letter-spacing: 1px; }
</style>
</head>
<body>
  <main class="flyer">
    <section class="panel panel--back">
      <div class="ornament-slot" role="img" aria-label="Kleines Kleeblatt-Ornament"></div>
      <div class="quote">
        <p><span class="initial">W</span>enn du nicht weißt wo du bist, kannst<br>du auch nicht wissen, wo du landest wenn<br>du dich auf den Weg machst.</p>
        <p>Selbst dann wenn du die Himmelsrichtungen<br>erkennst oder eine Karte besitzt.</p>
        <p>Erst musst du deinen Ausgangsort kennen...</p>
      </div>
      <address class="contact" style="font-style: normal;">
        <p>LumaWerk<br>8570 Lindenau</p>
        <p>Tel: 078 555 24 17<br>www.lumawerk-beratung.ch<br>info@lumawerk-beratung.ch</p>
      </address>
    </section>

    <section class="panel panel--front">
      <div class="photo" role="img" aria-label="Foto: zwei leuchtende Perlkugeln in einer geschwungenen Holzschale auf warmem beigem Grund mit Spiegelung"></div>
      <h1 class="title"><span class="initial">L</span>iebe Dich <span class="initial">S</span>elbst</h1>
      <p class="tagline">Dein Herz wird leuchten</p>
      <div class="brand">
        <span class="brand__dot"></span>
        <span class="brand__name">LumaWerk</span>
      </div>
    </section>
  </main>
</body>
</html>
```